catchy Z-Mug Coffee pods Box Design
Zarnifa
We want to design a retail box for our Z-mugs coffee pods. We need it to be catchy and give you a feeling that it is delicious! A lot off brands on the shelf so we need to appear professionally. We also prefer the simple designs but please use your full imagination. Our logo color is purple but you don't have to use it in the box. We sell the following z-mug pods now: Americano Coffee - Colombia Coffee - Breakfast Blend Coffe - Decaf Coffee - Red Tea - Tea With mint - Green Tea. We want to use colors to differentiate between each kind. We will attach some samples from the famous brands to get some ideas and you can yous your own ideas. We will attach our new logo. We want one face in English and the back face in arabic ( if you don't speak Arabic please just leave the back empty). Thank you.
yusuf-k yusuf-k
Hi Guys I attached the box die cut for your reference! Thank you all
Hi Guys This is the box size for the reference: https://www.filevornu.net/scl/fi/qp3vhz81tn5gdlre2mxob/box.pdf?rlkey=kd4ntz9e2ymbuaj0cwh5fqr7x&dl=0
Great job guys! Can we try the color red for the box?

```html
<!DOCTYPE html>
<html lang="en">
<head>
<meta charset="utf-8">
<title>Zarnifa Americano Z-Mug Pod Box – Dieline</title>
<link href="https://fonts.googleapis.com/css2?family=Poppins:wght@400;500;600;700;800&display=swap" rel="stylesheet">
<style>
  :root{
    --paper:#f4e8d9;
    --paper-deep:#ead8c2;
    --navy:#34315f;
    --ink:#2c2a4f;
    --bean:#8c5c3c;
    --cup-red:#b4282e;
    --eco-green:#3e9b4c;
    --stage:#ffffff;
    --line:#c9b8a3;
  }
  *{box-sizing:border-box;margin:0;padding:0}
  html,body{width:1200px;height:566px;overflow:hidden;background:var(--stage)}
  body{font-family:"Poppins",sans-serif;color:var(--ink);position:relative}

  .dieline{position:absolute;left:0;top:0;width:1200px;height:566px}
  .panel{position:absolute;background:var(--paper);overflow:hidden}
  .band-top,.band-bottom{position:absolute;left:0;right:0;background:var(--navy)}
  .band-top{top:0;height:8px}
  .band-bottom{bottom:0;height:46px}

  .glue-flap{position:absolute;left:203px;top:170px;width:30px;height:340px;background:var(--paper-deep);clip-path:polygon(0 6%,100% 0,100% 100%,0 94%)}

  /* Back panel */
  .panel-back{left:233px;top:150px;width:390px;height:380px;border-right:1px dashed var(--line)}
  .recycle-title{position:absolute;left:22px;top:28px;font-size:11px;font-weight:700;line-height:1.25;text-transform:uppercase;color:var(--navy);width:170px}
  .caution{position:absolute;left:22px;top:66px;display:flex;align-items:center;gap:6px;background:var(--navy);color:#fff;font-size:8px;font-weight:700;padding:3px 8px 3px 3px;border-radius:2px;text-transform:uppercase}
  .caution .step-num{width:14px;height:14px;background:#fff;color:var(--navy);display:flex;align-items:center;justify-content:center;font-size:9px}
  .steps{position:absolute;left:24px;top:100px;list-style:none;display:flex;flex-direction:column;gap:16px}
  .steps li{display:flex;align-items:center;gap:10px;font-size:9px;font-weight:700;color:var(--navy);text-transform:uppercase}
  .steps svg{width:18px;height:18px}
  .footnote{position:absolute;left:22px;top:222px;width:175px;font-size:6.5px;line-height:1.45;color:var(--ink)}
  .footnote strong{display:block;font-weight:600;margin-bottom:2px}
  .pod-tag{position:absolute;left:178px;top:22px;text-align:center;width:110px}
  .pod-tag .small-label{display:inline-block;background:var(--navy);color:#fff;font-size:6px;padding:1px 5px;font-weight:600}
  .pod-tag .tag-line{font-size:12px;font-weight:700;line-height:1.15;color:var(--navy)}
  .back-art{position:absolute;left:190px;top:88px;width:86px;height:112px;border-radius:6px;background:radial-gradient(circle at 50% 72%,var(--cup-red) 0 26%,transparent 27%),linear-gradient(180deg,#cfc6bb,#e8dccd)}
  .back-brand{position:absolute;left:280px;top:88px;width:100px}
  .value{font-size:8px;font-weight:700;color:var(--navy);letter-spacing:.5px}
  .wordmark{font-weight:800;color:var(--navy);letter-spacing:1px;text-transform:uppercase}
  .back-brand .wordmark{font-size:17px}
  .variety{font-size:6.5px;font-weight:600;color:var(--navy);letter-spacing:1px;text-transform:uppercase}

  /* Front panel */
  .panel-front{left:623px;top:150px;width:300px;height:380px;border-right:1px dashed var(--line)}
  .front-value{position:absolute;right:16px;top:16px}
  .front-tag{position:absolute;left:112px;top:18px;text-align:center}
  .front-tag .small-label{display:inline-block;background:var(--navy);color:#fff;font-size:6px;padding:1px 5px;font-weight:600}
  .front-tag .tag-line{font-size:14px;font-weight:700;line-height:1.1;color:var(--navy)}
  .front-brand{position:absolute;right:22px;top:74px;text-align:left;width:140px}
  .front-brand .wordmark{font-size:24px;line-height:1}
  .bean-art{position:absolute;right:14px;top:120px;width:120px;height:110px;border-radius:50%;background:radial-gradient(circle,rgba(140,92,60,.35),rgba(140,92,60,0) 70%)}
  .cup-art{position:absolute;left:26px;top:150px;width:130px;height:130px;border-radius:50%;background:radial-gradient(circle,#3a2218 0 30%,var(--cup-red) 31% 48%,#e2d2bf 49% 100%)}
  .front-copy{position:absolute;right:22px;top:236px;width:120px;font-size:6.5px;line-height:1.45}
  .front-foot{position:absolute;left:0;right:0;bottom:0;height:46px;display:flex;align-items:center;gap:8px;padding:0 14px;color:#fff}
  .pod-name{font-size:13px;font-weight:700;line-height:1;text-transform:uppercase}
  .pod-name small{display:block;font-size:7px;font-weight:500}
  .count{font-size:26px;font-weight:800;line-height:1}
  .eco-badge{width:22px;height:22px;background:var(--eco-green);border-radius:3px}
  .net-wt{margin-left:auto;font-size:6.5px;text-align:right}

  /* Side panel */
  .panel-side{left:923px;top:150px;width:75px;height:380px}
  .side-text{position:absolute;left:50%;top:50%;transform:translate(-50%,-50%) rotate(90deg);width:300px;display:flex;flex-direction:column;align-items:flex-start}
  .side-text .wordmark{font-size:16px}
  .side-text p{font-size:7px}

  /* Top flap */
  .top-flap{position:absolute;left:623px;top:40px;width:300px;height:110px;background:var(--paper);clip-path:polygon(0 100%,0 30%,8% 0,92% 0,100% 30%,100% 100%)}
  .top-flap .notch{position:absolute;left:138px;top:6px;width:24px;height:30px;background:var(--stage);clip-path:polygon(0 0,100% 0,80% 100%,20% 100%)}
  .dust-flap{position:absolute;top:118px;width:70px;height:32px;background:var(--paper-deep)}
  .dust-left{left:550px;clip-path:polygon(0 100%,15% 0,100% 0,100% 100%)}
  .dust-right{left:923px;clip-path:polygon(0 0,85% 0,100% 100%,0 100%)}
</style>
</head>
<body>
<div class="dieline">
  <div class="top-flap"><span class="notch"></span></div>
  <div class="dust-flap dust-left"></div>
  <div class="dust-flap dust-right"></div>
  <div class="glue-flap"></div>

  <section class="panel panel-back">
    <div class="band-top"></div>
    <h2 class="recycle-title">How to recycle Z-Mug pods in three steps</h2>
    <div class="caution"><span class="step-num">1</span>Caution: pod is hot</div>
    <ul class="steps">
      <li><svg viewBox="0 0 20 20"><path d="M3 15 L10 4 L17 15 Z" fill="none" stroke="#34315f" stroke-width="2"/></svg>Peel</li>
      <li><svg viewBox="0 0 20 20"><path d="M4 6 H16 L14 17 H6 Z" fill="#34315f"/></svg>Empty</li>
      <li><svg viewBox="0 0 20 20"><path d="M10 2 L16 12 H4 Z M6 14 H14 V18 H6 Z" fill="#34315f"/></svg>Recycle</li>
    </ul>
    <p class="footnote"><strong>*Lid must be fully removed before recycling</strong>Check local programs, as recycling may vary by area.</p>
    <div class="pod-tag"><span class="small-label">100%</span><div class="tag-line">Recyclable<br>Z-Mug Pod</div></div>
    <div class="back-art" role="img" aria-label="Red coffee cup beneath a pod being brewed"></div>
    <div class="back-brand">
      <div class="value">VALUE</div>
      <div class="wordmark">Zarnifa</div>
      <div class="variety">Americano</div>
    </div>
    <div class="band-bottom"></div>
  </section>

  <section class="panel panel-front">
    <div class="band-top"></div>
    <div class="value front-value">VALUE</div>
    <div class="front-tag"><span class="small-label">100%</span><div class="tag-line">Recyclable<br>Z-Mug Pod</div></div>
    <div class="front-brand">
      <div class="wordmark">Zarnifa</div>
      <div class="variety">Americano</div>
    </div>
    <div class="bean-art" role="img" aria-label="Scattered roasted coffee beans"></div>
    <div class="cup-art" role="img" aria-label="Red cup of black coffee seen from above"></div>
    <p class="front-copy">Smooth medium roast with a rich, balanced finish.</p>
    <footer class="band-bottom front-foot">
      <div class="pod-name">Z-Mug<small>pods</small></div>
      <div class="count">72</div>
      <span class="eco-badge"></span>
      <div class="net-wt">NET WT 9.5 OZ (270 g)</div>
    </footer>
  </section>

  <section class="panel panel-side">
    <div class="band-top"></div>
    <div class="side-text">
      <div class="wordmark">Zarnifa</div>
      <p>Medium roast coffee in recyclable pods</p>
    </div>
    <div class="band-bottom"></div>
  </section>
</div>
</body>
</html>
```